Looking for a cool & simple business-card-design for digital agency

Hi!

We are a web agency that offers Reputation Management, Zorvik & Seo Services and software development. We like cool things, we like innovative styles.

We have uploaded our logo.

Project Deadline Extended Reason: Client does not want any designs with the colorful logo. Please send us submissions ONLY with the blac and white logo. What the client would like to see:1) Back of the card: is a silver logo on a black background2) front of the card with all the data, please use white background and black logo thank you Added Friday, May 8, 2015

Software

```html
<!DOCTYPE html>
<html lang="en">
<head>
<meta charset="utf-8">
<title>Netvanta AG – Stationery</title>
<link rel="stylesheet" href="https://fonts.googleapis.com/css2?family=Jost:wght@300;400&display=swap">
<style>
  :root {
    --stage: #c4c4c6;
    --paper: #ffffff;
    --ink: #1d1d1d;
    --ink-soft: #4a4a4a;
    --dark: #1c1c1c;
    --silver: #b9b9b9;
    --silver-soft: #9a9a9a;
    --rule-light: #c9c9c9;
    --rule-dark: #3a3a3a;
  }
  * { box-sizing: border-box; margin: 0; padding: 0; }
  html, body { width: 1200px; height: 1200px; overflow: hidden; }
  body {
    position: relative;
    background: var(--stage);
    font-family: "Jost", "Helvetica Neue", Arial, sans-serif;
    font-weight: 300;
  }
  .sheet {
    position: absolute;
    overflow: hidden;
    box-shadow: 0 1px 4px rgba(0,0,0,0.25);
  }
  .wordmark {
    position: absolute;
    display: flex;
    align-items: center;
    gap: 0.4em;
    font-weight: 400;
    white-space: nowrap;
    letter-spacing: 0.02em;
  }
  .wordmark__square {
    width: 0.8em;
    height: 0.8em;
    background: currentColor;
    flex: none;
  }

  /* Business card – front */
  .card-front { left: 63px; top: 78px; width: 338px; height: 578px; background: var(--paper); color: var(--ink-soft); }
  .card-front .wordmark { left: 36px; top: 66px; font-size: 26px; color: var(--ink); }
  .card-front .services { position: absolute; left: 40px; top: 264px; font-size: 16px; line-height: 24px; }
  .card-front .rule { position: absolute; left: 40px; top: 357px; width: 252px; border-top: 1px solid var(--rule-light); }
  .card-front .address { position: absolute; left: 40px; top: 386px; font-size: 15px; line-height: 21px; }
  .card-front .contact { position: absolute; left: 40px; top: 443px; font-size: 15px; line-height: 21px; }

  /* Business card – back */
  .card-back { left: 435px; top: 78px; width: 339px; height: 578px; background: var(--dark); }
  .card-back .wordmark { left: 36px; top: 268px; font-size: 26px; color: var(--silver); }

  /* Letterhead */
  .letterhead { left: 585px; top: 315px; width: 555px; height: 710px; background: var(--paper); color: var(--ink); }
  .letterhead .wordmark { left: 50%; transform: translateX(-50%); top: 33px; font-size: 22px; }
  .letterhead .tagline { position: absolute; left: 0; right: 0; top: 65px; text-align: center; font-size: 8.5px; font-weight: 400; color: var(--ink-soft); }
  .letterhead .footer { position: absolute; left: 175px; top: 672px; font-size: 9px; line-height: 17px; color: var(--ink-soft); }

  /* Envelope */
  .envelope { left: 69px; top: 778px; width: 801px; height: 344px; background: var(--dark); color: var(--silver-soft); }
  .envelope .wordmark { left: 50px; top: 45px; font-size: 36px; color: var(--silver); }
  .envelope .services { position: absolute; left: 50px; top: 212px; font-size: 14px; line-height: 20px; }
  .envelope .rule { position: absolute; left: 50px; top: 260px; width: 360px; border-top: 1px solid var(--rule-dark); }
  .envelope .contact { position: absolute; left: 50px; top: 268px; font-size: 14px; line-height: 20px; }
</style>
</head>
<body>

  <section class="sheet card-front" aria-label="Business card front">
    <div class="wordmark"><span class="wordmark__square"></span>Netvanta AG</div>
    <p class="services">Reputation Management,<br>Zorvik &amp; Seo Services &amp;<br>software development</p>
    <div class="rule"></div>
    <p class="address">Dummy city Dummy country<br>Dummy land</p>
    <p class="contact">555.555.5555<br>ana.berg@mailhub.com<br>www.website.com</p>
  </section>

  <section class="sheet card-back" aria-label="Business card back">
    <div class="wordmark"><span class="wordmark__square"></span>Netvanta AG</div>
  </section>

  <section class="sheet letterhead" aria-label="Letterhead">
    <div class="wordmark"><span class="wordmark__square"></span>Netvanta AG</div>
    <p class="tagline">Reputation Management, Zorvik &amp; Seo Services &amp; software development</p>
    <p class="footer">Dummy city Dummy country Dummy land<br>555.555.5555 | www.website.com</p>
  </section>

  <section class="sheet envelope" aria-label="Envelope">
    <div class="wordmark"><span class="wordmark__square"></span>Netvanta AG</div>
    <p class="services">Reputation Management,<br>Zorvik &amp; Seo Services &amp; software development</p>
    <div class="rule"></div>
    <p class="contact">555.555.5555<br>ana.berg@mailhub.com | www.website.com</p>
  </section>

</body>
</html>
```